Belvoro Website

I need a website for a startup company that provides GIS (Geographic Information Services) staffing and products for local cities. Current website is www.belvorogroup.com

```html
<!DOCTYPE html>
<html lang="en">
<head>
<meta charset="utf-8">
<title>Belvoro Group — GIS Website</title>
<link href="https://fonts.googleapis.com/css2?family=Roboto:wght@400;500;700;800;900&display=swap" rel="stylesheet">
<style>
:root{
  --orange:#ff5212;
  --navy:#0b1d4f;
  --navy-deep:#0a1a45;
  --ink:#111318;
  --muted:#5b5f68;
  --faint:#c9cbd0;
  --panel:#efefef;
  --white:#ffffff;
  --blush:#fdece5;
}
*{margin:0;padding:0;box-sizing:border-box}
html,body{width:1200px;height:1200px;overflow:hidden;background:#fff;font-family:"Roboto",sans-serif;color:var(--ink)}
.canvas{position:relative;width:1200px;height:1200px;overflow:hidden}
.abs{position:absolute}
.btn{position:absolute;background:var(--orange);color:#fff;font-size:5.6px;font-weight:500;display:flex;align-items:center;justify-content:center;gap:4px;border-radius:2px;white-space:nowrap}
.h-display{font-weight:800;text-transform:uppercase;letter-spacing:-.3px;color:var(--ink)}
.fade{color:var(--faint)}
.label{font-size:4.4px;color:var(--muted)}
/* hero */
.hero{left:0;top:0;width:600px;height:322px;border-radius:0 0 10px 0;overflow:hidden;background:var(--navy-deep)}
.hero-photo{left:0;top:0;width:600px;height:281px;background:radial-gradient(ellipse at 55% 30%,#2f4c6a 0%,#1c3553 40%,#10243f 75%,#0c1d38 100%)}
.topbar{left:44px;top:4px;width:512px;height:13px;background:#0e2256;border-radius:4px 4px 0 0;color:#fff;font-size:4.6px;display:flex;align-items:center;padding-left:14px;gap:16px;white-space:nowrap}
.topbar .soc{margin-left:auto;display:flex;gap:10px;padding-right:6px}
.topbar .soc span{width:4px;height:4px;border-radius:50%;background:#fff;display:block}
.navbar{left:44px;top:17px;width:512px;height:29px;background:#f4f5f7;display:flex;align-items:center;white-space:nowrap}
.brand{display:flex;align-items:center;gap:4px;font-size:9.5px;font-weight:500;color:var(--orange);margin-left:16px}
.brand i{width:9px;height:9px;border-radius:50%;background:var(--orange);display:block}
.nav{display:flex;gap:13px;font-size:5.4px;font-weight:500;margin-left:72px}
.search{font-size:5px;color:#999;margin-left:28px}
.nav-cta{position:static;margin-left:12px;height:14px;width:57px}
.grid-btn{margin-left:auto;width:29px;height:29px;background:var(--orange)}
.hero-text{left:80px;top:112px;color:#fff}
.hero-text .count{font-size:5.5px}
.hero-text h1{font-size:22px;font-weight:800;line-height:21px;margin-top:6px;letter-spacing:-.4px}
.hero-text p{font-size:6px;line-height:10px;margin-top:12px;width:172px}
/* intro */
.intro{left:0;top:322px;width:600px;height:380px}
.intro h2{position:absolute;left:79px;top:45px;font-size:16.5px;line-height:17.8px;width:270px}
.card-img{position:absolute;top:113px;height:93px}
.card-white{position:absolute;left:178px;top:141px;width:139px;height:103px;background:#fff;box-shadow:0 4px 12px rgba(0,0,0,.06)}
.hatch{position:absolute;left:317px;top:219px;width:279px;height:22px;background:repeating-linear-gradient(135deg,#ececec 0 1px,transparent 1px 4px)}
/* about */
.about{left:4px;top:706px;width:591px;height:494px;background:var(--panel);border-radius:6px 6px 0 0}
.about h2{position:absolute;left:75px;top:43px;font-size:16.6px;line-height:17.8px;width:340px}
/* news */
.news{left:617px;top:38px;width:578px;height:350px;background:var(--panel);border-radius:8px}
.news h2{position:absolute;left:73px;top:42px;font-size:15.5px;line-height:17.5px}
.news-cards{position:absolute;left:73px;top:95px;width:433px;height:173px;background:#fff;border-radius:3px;display:flex}
.news-card{flex:1;padding:14px;border-right:1px solid #eee;position:relative}
.news-card:last-child{border-right:0}
.news-card .img{height:86px}
.date{position:absolute;left:14px;top:14px;width:30px;height:28px;background:#1b1f27;color:#fff;text-align:center;padding-top:4px}
.date b{font-size:10px;display:block;line-height:10px}
.date small{font-size:4.2px;letter-spacing:1px;display:block;margin-top:3px}
.news-card h3{font-size:8px;font-weight:500;line-height:9.6px;margin-top:32px}
/* contact */
.contact h2{position:absolute;left:690px;top:450px;font-size:15.5px;font-weight:800}
.field{position:absolute;left:690px;width:136px;border-bottom:1px solid #ddd;height:20px}
.field .label{display:block}
.field .val{font-size:5.3px;margin-top:3px;display:block}
/* newsletter */
.newsletter{left:617px;top:755px;width:578px;height:75px;background:var(--navy);border-radius:6px;overflow:hidden}
/* footer */
.footer{left:617px;top:834px;width:578px;height:361px;background:#f2f2f2;border-radius:6px}
.flink{font-size:5.2px;font-weight:500;line-height:13px}
.big{font-size:28px;font-weight:800;letter-spacing:-.6px;white-space:nowrap}
</style>
</head>
<body>
<div class="canvas">

  <!-- HERO -->
  <section class="abs hero">
    <div class="abs hero-photo" role="img" aria-label="Satellite view of the earth at night with highlighted city locations"></div>
    <div class="abs" style="left:553px;top:134px;width:1px;height:126px;background:rgba(255,255,255,.3)"></div>
    <div class="abs" style="left:553px;top:170px;width:1.5px;height:36px;background:#fff"></div>

    <div class="abs topbar">
      <span>✉ hello@northwindgis.co.uk</span>
      <span>☎ +44 20 7946 0321</span>
      <span>◷ Mon - Fri 8:30 - 17:30, Sat - Sun off</span>
      <div class="soc"><span></span><span></span><span></span><span></span></div>
    </div>
    <div class="abs navbar">
      <div class="brand"><i></i>Belvoro Group</div>
      <nav class="nav"><span>Home</span><span>About Us</span><span>Services</span><span>News</span><span>Contact Us</span></nav>
      <span class="search">⌕ Search...</span>
      <span class="btn nav-cta">Request A Quote</span>
      <span class="grid-btn"></span>
    </div>
    <div class="abs hero-text">
      <div class="count">02 <span style="opacity:.6">/ 03</span></div>
      <h1>PLANNING FOR<br>THE FUTURE</h1>
      <p>Make predictions and informed decisions that benefit both people and the planet</p>
    </div>
    <span class="btn" style="left:80px;top:209px;width:66px;height:20px">Discover More ›</span>
  </section>

  <!-- INTRO -->
  <section class="abs intro">
    <h2 class="h-display">To make sense of the immense amount of data in today's world, we can map it<span style="color:var(--faint)">.</span></h2>
    <div class="card-white"></div>
    <div class="card-img" style="left:192px;width:140px;background:linear-gradient(180deg,#c55b3a,#a9a49c 60%,#7b6f66)" role="img" aria-label="Warehouse aisle with stocked shelves and two workers"></div>
    <div class="card-img" style="left:344px;width:140px;background:linear-gradient(180deg,#5a5a5a,#9a9a9a 55%,#d2d2d2)" role="img" aria-label="Analyst at a desk in front of monitors, black and white"></div>
    <div class="card-img" style="left:495px;width:101px;background:linear-gradient(90deg,#2a2a2a,#8a8a8a 60%,#dcdcdc)" role="img" aria-label="Office workstation with computer screens, black and white"></div>
    <div class="abs" style="left:192px;top:215px;font-size:8px;font-weight:500">Spatial Analysis</div>
    <div class="abs" style="left:288px;top:216px;font-size:8px">‹ &nbsp; ›</div>
    <div class="hatch"></div>
    <div class="abs" style="left:79px;top:263px;font-size:7px;color:var(--orange);font-weight:500">◯ Play Video</div>
    <p class="abs" style="left:79px;top:282px;width:200px;font-size:6px;line-height:10px;color:var(--muted)">We show businesses how to gain a location data edge and we help everyone experience the benefits of the world outside</p>
    <span class="btn" style="left:79px;top:313px;width:80px;height:19px">Browse All Services ›</span>
  </section>

  <!-- ABOUT -->
  <section class="abs about">
    <h2 class="h-display">We ar<span class="fade">e an innovative team of</span> geospatial experts with 25 years of experience in the field of GIS. We specialize in providing results-driven GIS solutions for local government and the private sec<span class="fade">tor.</span></h2>
    <div class="abs" style="left:140px;top:166px;width:312px;height:1px;background:#888"></div>
    <div class="abs" style="left:75px;top:189px;width:102px;height:101px;background:linear-gradient(160deg,#d9dde2,#e96a35 60%,#c9c2b8)" role="img" aria-label="Surveyor looking through a surveying instrument"></div>
    <div class="abs" style="left:75px;top:297px;display:flex;gap:3px">
      <span style="border:1px solid var(--orange);color:var(--orange);font-size:4.5px;padding:1px 3px;border-radius:2px">Industrial</span>
      <span style="border:1px solid var(--orange);color:var(--orange);font-size:4.5px;padding:1px 3px;border-radius:2px">Goals</span>
    </div>
    <div class="abs" style="left:75px;top:312px;font-size:8px;font-weight:500">Surveying And Mapping</div>
    <p class="abs" style="left:75px;top:325px;width:104px;font-size:5.2px;line-height:8.5px;color:var(--muted)">Accurate, reliable surveying and mapping for precise land measurement and analysis.</p>
    <p class="abs" style="left:299px;top:189px;width:218px;font-size:6px;line-height:10.1px;color:var(--muted)">GIS connects data to a map, integrating location data (where things are) with all types of descriptive information (what things are like there). This provides a foundation for mapping and analysis that is used in science and almost every industry. GIS helps users understand patterns, relationships, and geographic context. The benefits include improved communication, efficiency, management, and decision-making.</p>
    <div class="abs" style="left:301px;top:267px;width:215px;height:214px;background:linear-gradient(180deg,#9c9fa3,#50606e 55%,#8c8f7d)" role="img" aria-label="Man with glasses studying a paper map at a table"></div>
    <div class="abs" style="left:320px;top:279px;display:flex;align-items:center;gap:5px;font-size:15px;font-weight:500;color:var(--orange)"><i style="width:15px;height:15px;border-radius:50%;background:var(--orange);display:block"></i>Belvoro Group</div>
  </section>

  <!-- NEWS -->
  <section class="abs news">
    <h2 class="h-display">News: Inn<span class="fade">ovations and trends<br>GIS</span></h2>
    <div class="news-cards">
      <div class="news-card">
        <div class="img" style="background:linear-gradient(180deg,#9aa5ad,#6a6f73 60%,#c9cdd0)" role="img" aria-label="Aerial view of an industrial area under clouds"></div>
        <div class="date"><b>15</b><small>AUG</small></div>
        <h3>Industrial Service Upgrades: Enhancing Efficiency And Performance</h3>
      </div>
      <div class="news-card">
        <div class="img" style="background:linear-gradient(120deg,#1c3a50,#d9582a 55%,#2b2b2b)" role="img" aria-label="Engineers using a glowing control panel"></div>
        <div class="date"><b>27</b><small>AUG</small></div>
        <h3>Industrial Services: Enhancing Efficiency And Performance Today</h3>
      </div>
      <div class="news-card">
        <div class="img" style="background:linear-gradient(180deg,#0d2a3a,#e0561f 55%,#1a1a1a)" role="img" aria-label="Brightly lit industrial hall at night"></div>
        <div class="date"><b>27</b><small>AUG</small></div>
        <h3>Urban Building Maintenance: Enhancing Efficiency And Sustainability Solutions</h3>
      </div>
    </div>
    <div class="abs" style="left:0;top:290px;width:578px;height:22px;background:repeating-linear-gradient(135deg,#e2e2e2 0 1px,transparent 1px 4px)"></div>
    <span class="btn" style="left:254px;top:290px;width:70px;height:19px">Browse All News ›</span>
  </section>

  <!-- CONTACT -->
  <section class="contact">
    <h2>GET IN TOUCH</h2>
    <div class="field" style="top:479px"><span class="label">Full Name:</span><span class="val">e.g. Daniel Marsh</span></div>
    <div class="field" style="top:507px"><span class="label">Company:</span><span class="val">e.g. Ridgeline LLC</span></div>
    <div class="field" style="top:536px"><span class="label">Phone:</span><span class="val">+44 20 7946 0321</span></div>
    <div class="field" style="top:564px"><span class="label">Email:</span><span class="val">hello@northwindgis.co.uk</span></div>
    <div class="field" style="top:592px"><span class="label">Address:</span><span class="val">e.g. Harborline LLC.</span></div>
    <div class="field" style="top:621px;height:43px"><span class="label">Message:</span><span class="val">Write your message here...</span></div>
    <span class="btn" style="left:690px;top:674px;width:58px;height:18px">Submit Now ›</span>
    <div class="abs" style="left:910px;top:392px;width:248px;height:266px;background:linear-gradient(160deg,#c9b48f,#4a6f7d 45%,#23303a 80%)" role="img" aria-label="GIS analyst with headset working at map screens by a window"></div>
    <div class="abs" style="left:910px;top:658px;width:124px;height:92px;background:var(--orange);color:#fff;padding:22px 17px">
      <div style="font-size:5px">Get To Know Us</div>
      <div style="font-size:6px;line-height:10px;margin-top:15px">845 E. Harlow Rd.<br>#204 Brea, CA<br>92821</div>
    </div>
    <div class="abs" style="left:1034px;top:658px;width:124px;height:92px;background:var(--blush);padding:22px 17px;font-size:5.2px;line-height:11px">
      <div style="color:var(--muted)">Get In Touch:</div>
      <div style="margin-top:8px"><span style="color:var(--orange)">✉</span> info@belvorogroup.com</div>
      <div><span style="color:var(--orange)">☎</span> +44 20 7946 0321</div>
      <div style="line-height:7px"><span style="color:var(--orange)">◷</span> Mon - Fri 8:30 - 17:30<br>&nbsp;&nbsp;&nbsp;Sat - Sun off</div>
    </div>
  </section>

  <!-- NEWSLETTER -->
  <section class="abs newsletter">
    <div class="abs" style="left:0;top:0;width:150px;height:75px;background:linear-gradient(90deg,#6b7f9a,#c4766a 55%,var(--navy))" role="img" aria-label="City skyline blended with a profile silhouette"></div>
    <h2 class="abs" style="left:153px;top:20px;font-size:11px;line-height:12px;font-weight:800;color:#fff">BOOST ENGAGEMENT WITH OUR<br>EXCLUSIVE NEWSLETTER<br>SUBSC<span style="color:#3a4d80">RIPTION TODAY!</span></h2>
    <div class="abs" style="left:355px;top:34px;width:106px;border-bottom:1px solid #fff;font-size:4.8px;color:#9aa5c4;padding-bottom:3px">Write your mail here...</div>
    <div class="abs" style="left:477px;top:36px;font-size:6px;color:#fff;font-weight:500">Submit ↗</div>
  </section>

  <!-- FOOTER -->
  <footer class="abs footer">
    <div class="abs" style="left:88px;top:38px;display:flex;align-items:center;gap:5px;font-size:12px;font-weight:500;color:var(--orange)"><i style="width:12px;height:12px;border-radius:50%;background:var(--orange);display:block"></i>Belvoro Group</div>
    <div class="abs" style="left:220px;top:33px">
      <div class="label" style="font-size:5.2px">Useful Links:</div>
      <div style="margin-top:6px" class="flink">Home<br>About Us<br>Services<br>News<br>Contact Us</div>
    </div>
    <div class="abs" style="left:424px;top:33px;font-size:5.2px;line-height:7px">
      <div class="label" style="font-size:5.2px">Get In Touch:</div>
      <div style="margin-top:10px"><span style="color:var(--orange)">●</span> 845 E. Harlow Rd.<br>&nbsp;&nbsp;&nbsp;#204 Brea, CA 92821</div>
      <div style="margin-top:6px"><span style="color:var(--orange)">✉</span> info@belvorogroup.com</div>
      <div style="margin-top:6px"><span style="color:var(--orange)">☎</span> +44 20 7946 0321</div>
    </div>
    <div class="abs" style="left:0;top:149px;width:578px;height:1px;background:#ddd"></div>
    <p class="abs" style="left:73px;top:169px;width:470px;font-size:4.6px;color:#8a8d93">Maximize your operational efficiency with our comprehensive GIS. Our team of experts offers top-tier maintenance, timely repairs, and tailored solutions to meet your unique needs.</p>
    <div class="abs" style="left:560px;top:149px;width:1px;height:47px;background:#ddd"></div>
    <div class="abs" style="left:564px;top:162px;font-size:4px;color:var(--orange);text-align:center;line-height:5px">↑<br>GO<br>TOP</div>
    <div class="abs" style="left:0;top:196px;width:578px;height:1px;background:#ddd"></div>
    <div class="abs" style="left:0;top:236px;width:578px;height:40px;overflow:hidden">
      <div class="abs big" style="left:-30px;top:0">SPATIAL ANALYSIS</div>
      <i class="abs" style="left:222px;top:6px;width:26px;height:26px;border-radius:50%;background:var(--orange)"></i>
      <div class="abs big" style="left:306px;top:0">COMMUNICATION</div>
      <i class="abs" style="left:552px;top:6px;width:26px;height:26px;border-radius:50%;background:var(--orange)"></i>
    </div>
    <div class="abs" style="left:0;top:321px;width:578px;height:1px;background:#ddd"></div>
    <div class="abs" style="left:73px;top:339px;font-size:5.2px;color:var(--muted)">©2024, <b style="color:var(--ink)">Belvoro Group.</b> All Rights Reserved.</div>
    <div class="abs" style="left:373px;top:339px;font-size:5.2px;display:flex;gap:11px"><span>Privacy Policy</span><span>Terms &amp; Conditions</span><span>Legal Info</span></div>
  </footer>

</div>
</body>
</html>
```